Create Stationary from existing logo(s)

We are looking for some assistance in tidying up the stationary that supports our brand. We are an innovative technology company, generally working with larger corporates. We have previously done a little work on brochures etc, but never really pulled it all together with our stationary.
In particular I am looking for:
1. A4 Letter Template for Letter (Microsoft Word 2007 template format)
2. A4 Template for Reports (Microsoft Word 2007 template format). This should include title page, table of contents, subsequent report pages including styles for tables, headings, and text.
3. Business Card Design - we will need to be able to edit the text, so the card should include sample text for name, title, phone number, mobile number, and email address.
4. Presentation Template (Microsoft Powerpoint 2007 template). See attached powerpoint which we quite like, but isn't really a template, and we have don't really use any consistent styles in it. The Powerpoint template needs to have a cover / title page, section break pages, and pages that may contain bullet point text, pictures, or a combination of bullet point text and pictures. We do like our current presentation, which gives some indication of our thinking.
I am attaching a brochure and the powerpoint presentation to give some indication of current materials. We are happy with the main concepts behind the brochure, and would not really be looking to change the key concepts unless you have a compelling reason. We do like the use of this secondary logo in the stationary related items
I have uploaded an eps file of the logo.

```html
<!DOCTYPE html>
<html lang="en">
<head>
<meta charset="utf-8">
<title>Lumenra – A4 Letter Template</title>
<link rel="stylesheet" href="https://fonts.googleapis.com/css2?family=Caladea:wght@400;700&display=swap">
<style>
  :root {
    --backdrop: #b3b7c0;
    --paper: #ffffff;
    --navy: #0d3f6e;
    --orange: #f39224;
    --placeholder: #5a6f9c;
    --salutation: #b8632a;
    --body-text: #3b3b3b;
    --brand: #1d5a9a;
  }
  * { box-sizing: border-box; margin: 0; padding: 0; }
  html, body { width: 1200px; height: 901px; overflow: hidden; background: var(--backdrop); }
  body { position: relative; font-family: "Caladea", "Cambria", Georgia, serif; }

  .letter-page {
    position: absolute; left: 276px; top: 0; width: 643px; height: 893px;
    background: var(--paper); overflow: hidden;
  }
  .page-frame { position: absolute; left: 0; top: 0; width: 643px; height: 893px; }

  .letter-content { position: absolute; left: 79px; top: 101px; width: 519px; color: var(--body-text); }
  .placeholder { color: var(--placeholder); }
  .date-line { font-size: 11px; line-height: 16px; }
  .recipient-block { margin-top: 22px; font-size: 11px; line-height: 16px; }
  .recipient-address { margin-top: 1px; font-size: 7.5px; line-height: 13.5px; }
  .salutation { margin-top: 20px; font-size: 11px; line-height: 16px; color: var(--salutation); }
  .letter-body p {
    margin-top: 10px; font-size: 12.4px; line-height: 14.4px; text-align: justify;
  }
  .letter-body p:first-child { margin-top: 14px; }
  .closing { margin-top: 12px; font-size: 11px; line-height: 16px; }
  .signature-block { margin-top: 32px; font-size: 11px; line-height: 17px; }

  .brand-name {
    position: absolute; left: 26px; top: 812px;
    font-size: 28px; line-height: 30px; font-weight: 400; color: var(--navy);
  }
</style>
</head>
<body>
  <main class="letter-page">
    <svg class="page-frame" viewBox="0 0 643 893" aria-hidden="true">
      <rect x="0" y="0" width="643" height="60" fill="var(--navy)"/>
      <path d="M0,110 C0,60 40,35 110,35 L643,35 L643,110 Z" fill="var(--paper)"/>
      <path d="M0,866 L480,866 C590,866 640,850 643,812 L643,893 L0,893 Z" fill="var(--orange)"/>
    </svg>

    <article class="letter-content">
      <p class="date-line placeholder">Date: [Insert Date]</p>

      <div class="recipient-block placeholder">
        <p>[Recipient]</p>
        <p>[Title]</p>
        <div class="recipient-address">
          <p>[Company]</p>
          <p>[Address 1]</p>
          <p>[Address 2]</p>
          <p>[Address 3]</p>
        </div>
      </div>

      <p class="salutation">Dear [Recipient]:</p>

      <div class="letter-body">
        <p>Fusce neque mi, consectetuer gravida, convallis ac, varius a, pede. Fusce pellentesque pretium quam. Ut luctus, justo id volutpat iaculis, est diam pulvinar sem, quis bibendum turpis dui eget mauris. Sed in mauris. Ut massa. Pellentesque condimentum felis nec sapien. Integer posuere elit at turpis. Nulla facilisi. Sed sapien ipsum, commodo ut, facilisis vitae, ultrices non, metus. Aenean non nulla. Curabitur molestie volutpat magna. Vestibulum tempor faucibus nisi. Pellentesque vitae enim.</p>
        <p>Aliquam rhoncus volutpat mauris. Sed auctor. Donec tincidunt velit et tellus. Donec sed augue eget lacus placerat adipiscing. Ut convallis suscipit nulla. Morbi posuere ullamcorper ligula. Duis sit amet odio nec lorem ornare gravida. Suspendisse ante nulla, gravida quis, eleifend sit amet, placerat eget, purus. Sed egestas magna ut erat. Vivamus euismod, odio id mattis porttitor, tellus nisl consectetuer turpis, ut auctor enim justo euismod nulla. Fusce eget diam vulputate massa tempor tempor.</p>
        <p>In ante. Phasellus convallis, nisl in vestibulum facilisis, lacus pede bibendum urna, dapibus pellentesque eros magna sed nibh. Etiam tortor arcu, porta nec, laoreet quis, mollis in, libero. Aenean dapibus est a metus. In sit amet elit. Pellentesque luctus lacus scelerisque arcu. Cras mattis diam. Sed molestie, lectus id bibendum luctus, magna orci luctus quam, et auctor urna diam sit amet ligula. Sed purus dui, suscipit et, malesuada non, consectetuer in, augue. Proin et sapien. Maecenas aliquam, nibh id aliquet tincidunt, ante neque pulvinar mauris, sit amet fermentum nibh augue mollis risus. Mauris porttitor varius mauris. Vivamus in urna et sem accumsan imperdiet. Aenean fringilla, eros tincidunt gravida elementum, justo eros pharetra felis, in rhoncus arcu lectus non enim. Phasellus odio tortor, mattis ut, mattis elementum, luctus at, orci.</p>
      </div>

      <p class="closing">Sincerely,</p>

      <div class="signature-block placeholder">
        <p>[Your Name]</p>
        <p>[Your Title]</p>
      </div>
    </article>

    <p class="brand-name">Lumenra</p>
  </main>
</body>
</html>
```